Vero-Shine Janitorial Services

Looking for a modern design for my new business. I like the clear see through of the card I've attached. The business is built around The Brightwell Omni 720 system, with that said I'd like to add the brightwell logo on the bachside with the statement of Powered by (then the Brightwell Logo). I really like the layout and color schemes of the card I attached. Black, Blue, and White. I would like to incorporate three images into the diamond shape, as seem in the layout.

Martin Okafor
Managing Partner

Still waiting on revisions?

```html
<!DOCTYPE html>
<html lang="en">
<head>
<meta charset="utf-8">
<title>Vero-Shine Janitorial Services – Business Card</title>
<link rel="stylesheet" href="https://fonts.googleapis.com/css2?family=Roboto:wght@400;700&display=swap">
<style>
  :root {
    --blue-brand: #2a66b5;
    --blue-deep: #2465b0;
    --blue-bright: #29b3e8;
    --blue-soft: #5fb8e6;
    --ink-text: #3d4148;
    --paper: #ffffff;
  }
  html, body {
    margin: 0;
    padding: 0;
    overflow: hidden;
    background: var(--paper);
  }
  .card {
    position: relative;
    width: 1200px;
    height: 685px;
    background: var(--paper);
    overflow: hidden;
    font-family: "Roboto", Arial, sans-serif;
  }
  .card__waves {
    position: absolute;
    inset: 0;
    width: 1200px;
    height: 685px;
  }
  .brand {
    position: absolute;
    left: 564px;
    top: 30px;
    width: 400px;
    text-align: center;
    color: var(--ink-text);
    font-family: "Roboto", Arial, sans-serif;
    font-weight: 400;
  }
  .brand__dot {
    display: block;
    width: 200px;
    height: 200px;
    margin: 0 auto;
    border-radius: 50%;
    background: var(--blue-soft);
  }
  .brand__name {
    margin: 34px 0 0;
    font-size: 50px;
    font-weight: 400;
    line-height: 1;
  }
  .brand__tagline {
    margin: 12px 0 0;
    font-size: 24px;
    font-weight: 400;
    letter-spacing: 1px;
  }
  .person {
    position: absolute;
    left: 34px;
    top: 368px;
    display: flex;
    align-items: flex-start;
    gap: 30px;
  }
  .person__icon { width: 48px; height: 48px; margin-top: 8px; }
  .person__name {
    margin: 0;
    font-size: 39px;
    font-weight: 700;
    color: var(--blue-brand);
    line-height: 1.05;
  }
  .person__title {
    margin: 4px 0 0;
    font-size: 24px;
    color: var(--ink-text);
  }
  .divider {
    position: absolute;
    left: 0;
    top: 465px;
    width: 1070px;
    height: 8px;
    background: linear-gradient(90deg, var(--blue-brand) 0%, #6f95cf 45%, rgba(255,255,255,0) 100%);
  }
  .contacts {
    position: absolute;
    left: 34px;
    top: 496px;
    margin: 0;
    padding: 0;
    list-style: none;
  }
  .contacts__item {
    display: flex;
    align-items: flex-start;
    gap: 34px;
    font-size: 26px;
    color: var(--ink-text);
    line-height: 34px;
    margin-bottom: 11px;
  }
  .contacts__icon { width: 46px; height: 46px; flex: none; }
  .contacts__item--address .contacts__icon { height: 58px; }
</style>
</head>
<body>
<main class="card">
  <svg class="card__waves" viewBox="0 0 1000 571" preserveAspectRatio="none" aria-hidden="true">
    <defs>
      <linearGradient id="wave-band" x1="0" y1="0" x2="0" y2="1">
        <stop offset="0" stop-color="#1e6fbf"/>
        <stop offset="0.45" stop-color="#29b3e8"/>
        <stop offset="1" stop-color="#8fd3f3"/>
      </linearGradient>
    </defs>
    <path d="M772,0 C815,80 845,160 895,235 C965,340 945,460 868,571 L1000,571 L1000,0 Z" fill="#b9e3f7"/>
    <path d="M800,0 C840,90 880,170 915,250 C965,360 950,470 905,571 L1000,571 L1000,0 Z" fill="url(#wave-band)"/>
    <path d="M828,0 C825,90 860,180 905,250 C945,320 960,430 932,571 L1000,571 L1000,0 Z" fill="#2465b0"/>
  </svg>

  <header class="brand">
    <span class="brand__dot" aria-hidden="true"></span>
    <h1 class="brand__name">Vero-Shine</h1>
    <p class="brand__tagline">Janitorial Services</p>
  </header>

  <section class="person">
    <svg class="person__icon" viewBox="0 0 48 48" aria-hidden="true">
      <circle cx="24" cy="13" r="11" fill="var(--blue-brand)"/>
      <path d="M2,46 C2,31 12,26 24,26 C36,26 46,31 46,46 Z" fill="var(--blue-brand)"/>
    </svg>
    <div>
      <h2 class="person__name">FULL NAME</h2>
      <p class="person__title">Job Title</p>
    </div>
  </section>

  <div class="divider" aria-hidden="true"></div>

  <ul class="contacts">
    <li class="contacts__item">
      <svg class="contacts__icon" viewBox="0 0 24 24" aria-hidden="true">
        <path fill="var(--blue-brand)" d="M6.6 10.8a15.1 15.1 0 0 0 6.6 6.6l2.2-2.2a1 1 0 0 1 1-.25 11.4 11.4 0 0 0 3.6.57 1 1 0 0 1 1 1V20a1 1 0 0 1-1 1A17 17 0 0 1 3 4a1 1 0 0 1 1-1h3.5a1 1 0 0 1 1 1c0 1.25.2 2.45.57 3.57a1 1 0 0 1-.25 1z"/>
      </svg>
      <span>PHONE NUMBER</span>
    </li>
    <li class="contacts__item">
      <svg class="contacts__icon" viewBox="0 0 24 24" aria-hidden="true">
        <rect x="2" y="5" width="20" height="14" fill="var(--blue-brand)"/>
        <path d="M2.5 5.5 L12 13 L21.5 5.5 M2.5 18.5 L9.5 11 M21.5 18.5 L14.5 11" stroke="#fff" stroke-width="1.3" fill="none"/>
      </svg>
      <span>EMAIL ADDRESS</span>
    </li>
    <li class="contacts__item contacts__item--address">
      <svg class="contacts__icon" viewBox="0 0 24 30" aria-hidden="true">
        <path fill="var(--blue-brand)" d="M12 1a10 10 0 0 0-10 10c0 7.5 10 18 10 18s10-10.5 10-18A10 10 0 0 0 12 1z"/>
        <circle cx="12" cy="11" r="3.6" fill="#fff"/>
      </svg>
      <span>ADDRESS LINE 1<br>ADDRESS LINE 2</span>
    </li>
  </ul>
</main>
</body>
</html>
```